Business Card Design

Please copy the format of the attached card.

FRONT:
White text small blue horses head logo where "mirun" in in example

BACK:
Blue background w/ white horses head

Industry/Entity Type

Business

Contact Information for Business Card

Calvin Ostrow
Chief Executive Officer
Halvern Lodges & Resorts
412 Lindmoor Street | San Francisco, California 94109
Tel: +1.555.482.1937
email: calvin@halvernlodges.example

```html
<!DOCTYPE html>
<html lang="en">
<head>
<meta charset="utf-8">
<title>Halvern Lodges &amp; Resorts – Business Card Back</title>
<link rel="stylesheet" href="https://fonts.googleapis.com/css2?family=Arimo:wght@400&display=swap">
<style>
  :root {
    --card-blue: #1f4079;
    --card-white: #ffffff;
  }
  html, body {
    margin: 0;
    padding: 0;
    width: 1200px;
    height: 741px;
    overflow: hidden;
    background: var(--card-blue);
  }
  .card-back {
    position: relative;
    width: 1200px;
    height: 741px;
    background: var(--card-blue);
    color: var(--card-white);
    font-family: "Arimo", Arial, sans-serif;
  }
  .brand-mark {
    position: absolute;
    left: 0;
    right: 0;
    top: 262px;
    display: flex;
    justify-content: center;
    align-items: center;
    gap: 14px;
  }
  .brand-mark__dot {
    width: 18px;
    height: 18px;
    border-radius: 50%;
    background: var(--card-white);
  }
  .brand-mark__name {
    font-size: 60px;
    font-weight: 400;
    line-height: 1;
  }
  .company-name {
    position: absolute;
    left: 0;
    right: 0;
    top: 402px;
    margin: 0;
    text-align: center;
    font-size: 51px;
    font-weight: 400;
    line-height: 1;
  }
  .website {
    position: absolute;
    left: 0;
    right: 0;
    top: 548px;
    margin: 0;
    text-align: center;
    font-size: 23px;
    font-weight: 400;
    letter-spacing: 0.36em;
    line-height: 1;
  }
</style>
</head>
<body>
  <main class="card-back">
    <div class="brand-mark">
      <span class="brand-mark__dot"></span>
      <span class="brand-mark__name">Halvern</span>
    </div>
    <h1 class="company-name">Halvern Lodges &amp; Resorts</h1>
    <p class="website">www.halvernlodges.example</p>
  </main>
</body>
</html>
```